Professional business cards for real estate development company

I need business cards for my new real estate development company. The company, "KORVA" is a real estate development, investment, and advisory firm with a focus on multifamily, office, and mixed-use projects across primary and secondary markets in the Southeast United States.

Style preference is modern

Industry/Entity Type

Real Estate Development

Contact Information for Business Card

The business cards need to include:
Name
Title
Mailing Address
Phone Number
Web Address

Logo is attached. I would like white to be the primary color with incorporation of the company colors: #232D3A and #B5A451

Font styles to use
Other font styles liked:
• Montserrat, Avenir

Requirements
Must have
• Company Logo. No need to include the company name since the name is in the logo.
Should not have
• No line type designs

```html
<!DOCTYPE html>
<html lang="en">
<head>
<meta charset="utf-8">
<title>KORVA Business Cards</title>
<link rel="stylesheet" href="https://fonts.googleapis.com/css2?family=Montserrat:wght@500;600;700&display=swap">
<style>
  :root {
    --navy: #232D3A;
    --gold: #B5A451;
    --paper: #ffffff;
    --backdrop: #cfcfcf;
  }
  * { box-sizing: border-box; margin: 0; padding: 0; }
  html, body { width: 1200px; height: 900px; overflow: hidden; }
  body {
    background: var(--backdrop);
    font-family: "Montserrat", sans-serif;
    color: var(--navy);
    display: flex;
    flex-direction: column;
    align-items: center;
    justify-content: center;
    gap: 40px;
  }
  .card {
    position: relative;
    width: 640px;
    height: 366px;
    background: var(--paper);
    box-shadow: 0 6px 18px rgba(0,0,0,0.18);
  }
  /* Front */
  .front-mark {
    position: absolute;
    left: 250px;
    top: 138px;
    display: flex;
    align-items: center;
    gap: 22px;
  }
  .wordmark {
    font-weight: 700;
    font-size: 40px;
    letter-spacing: 4px;
    color: var(--navy);
  }
  .tagline {
    display: flex;
    align-items: stretch;
    gap: 10px;
  }
  .tagline-text {
    font-weight: 600;
    font-size: 14px;
    line-height: 17px;
    text-align: right;
    text-transform: uppercase;
  }
  .gold-bar {
    width: 4px;
    background: var(--gold);
  }
  /* Back */
  .back-logo {
    position: absolute;
    left: 60px;
    top: 120px;
    display: flex;
    align-items: center;
    gap: 10px;
  }
  .logo-square {
    width: 14px;
    height: 14px;
    background: var(--navy);
  }
  .back-logo .wordmark { font-size: 42px; }
  .address {
    position: absolute;
    left: 60px;
    bottom: 44px;
    font-weight: 500;
    font-size: 15px;
    line-height: 20px;
  }
  .person {
    position: absolute;
    left: 380px;
    top: 70px;
    display: flex;
    gap: 10px;
  }
  .person .gold-bar { width: 4px; }
  .person-name {
    font-weight: 700;
    font-size: 19px;
    color: var(--gold);
    text-transform: uppercase;
  }
  .person-title {
    font-weight: 600;
    font-size: 12px;
    text-transform: uppercase;
    margin-top: 2px;
  }
  .contacts {
    position: absolute;
    left: 380px;
    top: 210px;
    list-style: none;
    font-weight: 500;
    font-size: 13.5px;
    line-height: 22px;
  }
  .contacts li { display: flex; align-items: center; gap: 7px; }
  .contacts svg { width: 12px; height: 12px; fill: var(--gold); flex: none; }
</style>
</head>
<body>
  <section class="card card-front">
    <div class="front-mark">
      <span class="wordmark">KORVA</span>
      <div class="tagline">
        <p class="tagline-text">Commercial<br>Real Estate<br>Platform</p>
        <span class="gold-bar"></span>
      </div>
    </div>
  </section>

  <section class="card card-back">
    <div class="back-logo">
      <span class="logo-square"></span>
      <span class="wordmark">KORVA</span>
    </div>

    <p class="address">4120 Alder Crest Way NE<br>Atlanta, Georgia 30309</p>

    <div class="person">
      <span class="gold-bar"></span>
      <div>
        <p class="person-name">Dana Whitlock</p>
        <p class="person-title">Partner</p>
      </div>
    </div>

    <ul class="contacts">
      <li>
        <svg viewBox="0 0 24 24" aria-hidden="true"><path d="M6.6 10.8a15 15 0 0 0 6.6 6.6l2.2-2.2c.3-.3.7-.4 1-.2 1.1.4 2.3.6 3.6.6.6 0 1 .4 1 1V20c0 .6-.4 1-1 1A17 17 0 0 1 3 4c0-.6.4-1 1-1h3.5c.6 0 1 .4 1 1 0 1.3.2 2.5.6 3.6.1.3 0 .7-.2 1z"/></svg>
        (555) 014-2290
      </li>
      <li>
        <svg viewBox="0 0 24 24" aria-hidden="true"><path d="M2 5h20v14H2zm2 2v.5l8 5 8-5V7zm0 3v7h16v-7l-8 5z"/></svg>
        info@korvadevelopment.com
      </li>
      <li>
        <svg viewBox="0 0 24 24" aria-hidden="true"><path d="M12 2a10 10 0 1 0 0 20 10 10 0 0 0 0-20zm6.9 9h-3a15 15 0 0 0-1.3-6 8 8 0 0 1 4.3 6zM12 4c1 1.4 1.8 3.9 1.9 7h-3.8C10.2 7.9 11 5.4 12 4zM9.4 5a15 15 0 0 0-1.3 6h-3a8 8 0 0 1 4.3-6zm-4.3 8h3a15 15 0 0 0 1.3 6 8 8 0 0 1-4.3-6zM12 20c-1-1.4-1.8-3.9-1.9-7h3.8c-.1 3.1-.9 5.6-1.9 7zm2.6-1a15 15 0 0 0 1.3-6h3a8 8 0 0 1-4.3 6z"/></svg>
        www.korvadevelopment.com
      </li>
    </ul>
  </section>
</body>
</html>
```